Looking for fresh and exciting business card design that is simple and yet eye catching and impactfu

I am starting my own independent Marketing Communications consultancy with aim to service a small group of clients. Focus on aviation, travel and hospitality industries. Name of the consultancy is RVB BizLink or RVB Marketing Communications. Basic content of the card will be
RVB Marketing Communications / RVB BizLink
Greta Holm Vasquez
Email
Mobile
Website

Target Market(s)

Aviation, travel and hospitality industries

Industry/Entity Type

Travel

Contact Information for Business Card

Greta Holm Vasquez
Consultant
gretahkv@mailbrook.example
Mobile : +86 1502 846 2071
Skype: gretabluecanvas

Font styles to use
Sans Serif
Script

Requirements
Must have
• Professional look and feel.
Nice to have
• Fresh, contrast. I don't have a logo so using the company name to create a focal point.
Should not have
• Too many colors.

```html
<!DOCTYPE html>
<html lang="en">
<head>
<meta charset="utf-8">
<title>RVB Marketing Communications – Business Cards</title>
<link rel="stylesheet" href="https://fonts.googleapis.com/css2?family=Kreon:wght@300;400&family=Open+Sans:wght@400&display=swap">
<style>
  :root {
    --backdrop: #e6e7e8;
    --charcoal: #2a2a2b;
    --slate: #6b6b6d;
    --teal-deep: #1fa3aa;
    --teal-bright: #45c3c8;
    --paper: #f6f6f6;
    --white: #ffffff;
    --ink-grey: #5d5d5f;
  }
  * { box-sizing: border-box; margin: 0; padding: 0; }
  html, body { width: 1200px; height: 873px; overflow: hidden; }
  body {
    background: var(--backdrop);
    display: flex;
    align-items: center;
    justify-content: center;
    gap: 80px;
  }
  .card {
    width: 330px;
    height: 500px;
    position: relative;
    box-shadow: 0 6px 18px rgba(0,0,0,0.12);
  }
  .brand-name {
    font-family: "Kreon", Georgia, serif;
    font-weight: 300;
    color: var(--white);
    line-height: 1.05;
    text-align: center;
  }

  /* Front */
  .card-front { background: var(--charcoal); padding: 22px; }
  .front-frame {
    height: 100%;
    background: var(--white);
    padding: 8px;
  }
  .front-panel {
    height: 100%;
    background: var(--teal-deep);
    display: flex;
    align-items: flex-end;
    justify-content: flex-end;
    padding: 0 22px 26px 0;
  }
  .front-panel .brand-name { font-size: 22px; }
  .front-panel .brand-initials { font-size: 30px; display: block; margin-bottom: 2px; }

  /* Back */
  .card-back { background: var(--paper); padding: 20px; display: flex; flex-direction: column; }
  .back-header {
    height: 150px;
    background: var(--slate);
    display: flex;
    align-items: center;
    justify-content: flex-end;
    padding-right: 28px;
  }
  .back-header .brand-name { font-size: 21px; }
  .back-header .brand-initials { font-size: 28px; display: block; margin-bottom: 2px; }
  .name-band {
    background: var(--teal-bright);
    margin-top: 10px;
    padding: 14px 0 10px 26px;
  }
  .person-name {
    font-family: "Kreon", Georgia, serif;
    font-weight: 300;
    font-size: 20px;
    color: var(--white);
  }
  .person-role {
    font-family: "Open Sans", Arial, sans-serif;
    font-size: 8px;
    color: var(--white);
    margin-left: 4px;
  }
  .office-band {
    margin: 8px 0;
    padding: 7px 0 7px 20px;
    border-top: 2px solid var(--teal-bright);
    border-bottom: 2px solid var(--teal-bright);
    font-family: "Kreon", Georgia, serif;
    font-size: 21px;
    color: var(--ink-grey);
  }
  .contact-block {
    flex: 1;
    background: var(--teal-bright);
    padding: 20px 0 0 26px;
    list-style: none;
  }
  .contact-block li {
    font-family: "Open Sans", Arial, sans-serif;
    font-size: 11.5px;
    color: var(--white);
    line-height: 2.1;
  }
</style>
</head>
<body>
  <article class="card card-front" aria-label="Card front">
    <div class="front-frame">
      <div class="front-panel">
        <p class="brand-name"><span class="brand-initials">RVB</span>Marketing<br>Communications</p>
      </div>
    </div>
  </article>

  <article class="card card-back" aria-label="Card back">
    <header class="back-header">
      <p class="brand-name"><span class="brand-initials">RVB</span>Marketing<br>Communications</p>
    </header>
    <div class="name-band">
      <p class="person-name">Greta Holm Vasquez</p>
      <p class="person-role">consultant</p>
    </div>
    <p class="office-band">RVB BizLink</p>
    <ul class="contact-block">
      <li>gretahkv@mailbrook.example</li>
      <li>Mobile : +86 1502 846 2071</li>
      <li>Skype: gretabluecanvas</li>
    </ul>
  </article>
</body>
</html>
```